Calvoterra business card

a nice business card with the logo,
Calvoterra
Teresa Lindqvist
Marketing Director
CH-1563 Castelmont
Verdania
+41 76 382 1904
email: Teresa.Lindqvist@calvoterra-mail.example

Target Market(s)

fertilizer business people, very nice and classic business card, normal size, make it nice and funky, try to make it different from the normal boring ones if possible.

Industry/Entity Type

Farming

Number of Pages Required

1 page

Requirements
Must have
• logo, Calvoterra, my name - mail and phone number
regular business card size for me to print easy please

```html
<!DOCTYPE html>
<html lang="en">
<head>
<meta charset="utf-8">
<title>Calvoterra business card</title>
<link rel="stylesheet" href="https://fonts.googleapis.com/css2?family=Fira+Sans:wght@400;500;600&display=swap">
<style>
  :root {
    --canvas: #808080;
    --card-white: #ffffff;
    --logo-tile: #fafafa;
    --leaf: #a8cc1f;
    --leaf-deep: #8faf12;
    --leaf-text: #a4c81c;
    --ink-light: #ffffff;
    --brand-grey: #8a8a8a;
  }
  * { box-sizing: border-box; margin: 0; padding: 0; }
  html, body {
    width: 1200px; height: 1079px; overflow: hidden;
    background: var(--canvas);
    font-family: "Fira Sans", Arial, sans-serif;
  }
  .sheet { position: relative; width: 1200px; height: 1079px; }
  .card {
    position: absolute; width: 490px; height: 302px;
    background: var(--card-white); overflow: hidden;
  }
  .card--front-a { left: 33px; top: 17px; }
  .card--front-b { left: 672px; top: 17px; }
  .card--solid { left: 33px; top: 372px; background: var(--leaf); }
  .card--wave { left: 672px; top: 372px; }
  .card--split-left { left: 31px; top: 730px; height: 300px; }
  .card--split-right { left: 672px; top: 730px; height: 300px; }

  .brand-tile {
    position: absolute; background: var(--logo-tile);
    display: flex; flex-direction: column; align-items: center; justify-content: flex-end;
  }
  .brand-tile__dot {
    width: 46px; height: 46px; border-radius: 50%;
    background: var(--leaf); margin-bottom: 34px;
  }
  .brand-tile__name {
    color: var(--brand-grey); font-weight: 500; font-size: 13px;
    letter-spacing: 4px; text-transform: uppercase; margin-bottom: 20px;
  }
  .card--front-a .brand-tile,
  .card--front-b .brand-tile { left: 132px; top: 36px; width: 207px; height: 217px; }

  .contact { position: absolute; color: var(--ink-light); }
  .contact__name { font-weight: 500; font-size: 31px; line-height: 1; }
  .contact__role { font-weight: 500; font-size: 17px; margin-top: 8px; }
  .contact__lines { font-weight: 500; font-size: 21px; line-height: 28px; }

  .card--solid .contact { left: 22px; top: 28px; }
  .card--solid .contact__lines { margin-top: 56px; }

  .card--wave .contact { left: 26px; top: 24px; color: var(--leaf-text); }
  .card--wave .contact__name { font-size: 29px; }
  .card--wave .contact__lines { margin-top: 40px; font-size: 20px; line-height: 26px; }
  .wave { position: absolute; left: 0; bottom: 0; width: 490px; height: 80px; }

  .panel-green { position: absolute; top: 0; height: 100%; background: var(--leaf); }
  .card--split-left .panel-green { left: 202px; right: 0; }
  .card--split-right .panel-green { left: 0; width: 287px; }
  .card--split-left .brand-tile { left: 8px; top: 55px; width: 170px; height: 172px; }
  .card--split-right .brand-tile { left: 306px; top: 63px; width: 157px; height: 173px; }
  .card--split-left .brand-tile__dot,
  .card--split-right .brand-tile__dot { width: 38px; height: 38px; margin-bottom: 30px; }
  .card--split-left .brand-tile__name,
  .card--split-right .brand-tile__name { font-size: 11px; letter-spacing: 3px; margin-bottom: 16px; }

  .card--split-left .contact { left: 221px; top: 52px; }
  .card--split-right .contact { left: 19px; top: 52px; }
  .split .contact__name { font-size: 27px; }
  .split .contact__role { font-size: 16px; margin-top: 6px; }
  .split .contact__address { font-size: 17px; line-height: 23px; margin-top: 38px; font-weight: 500; }
  .split .contact__reach { font-size: 15px; line-height: 22px; margin-top: 32px; font-weight: 500; }
  .split .contact__email { font-size: 12.6px; letter-spacing: -0.1px; }
</style>
</head>
<body>
<main class="sheet">
  <section class="card card--front-a">
    <div class="brand-tile"><span class="brand-tile__dot"></span><span class="brand-tile__name">Calvoterra</span></div>
  </section>
  <section class="card card--front-b">
    <div class="brand-tile"><span class="brand-tile__dot"></span><span class="brand-tile__name">Calvoterra</span></div>
  </section>

  <section class="card card--solid">
    <div class="contact">
      <p class="contact__name">Teresa Lindqvist</p>
      <p class="contact__role">Marketing Director</p>
      <div class="contact__lines">
        <p>CH-1563 Castelmont</p>
        <p>Verdania</p>
        <p>+41 76 382 1904</p>
        <p>Teresa.Lindqvist@calvoterra-mail.example</p>
      </div>
    </div>
  </section>

  <section class="card card--wave">
    <div class="contact">
      <p class="contact__name">Teresa Lindqvist</p>
      <p class="contact__role">Marketing Director</p>
      <div class="contact__lines">
        <p>CH-1563 Castelmont</p>
        <p>Verdania</p>
        <p>+41 76 382 1904</p>
        <p>Teresa.Lindqvist@calvoterra-mail.example</p>
      </div>
    </div>
    <svg class="wave" viewBox="0 0 490 80" preserveAspectRatio="none" aria-hidden="true">
      <path d="M0 30 C90 8 160 58 250 40 C330 24 400 6 490 30 L490 80 L0 80 Z" fill="var(--leaf-deep)"/>
      <path d="M0 42 C90 20 160 70 250 52 C330 36 400 18 490 42 L490 80 L0 80 Z" fill="var(--leaf)"/>
    </svg>
  </section>

  <section class="card card--split-left split">
    <div class="brand-tile"><span class="brand-tile__dot"></span><span class="brand-tile__name">Calvoterra</span></div>
    <div class="panel-green"></div>
    <div class="contact">
      <p class="contact__name">Teresa Lindqvist</p>
      <p class="contact__role">Marketing Director</p>
      <div class="contact__address"><p>CH-1563 Castelmont</p><p>Verdania</p></div>
      <div class="contact__reach"><p>+41 76 382 1904</p><p class="contact__email">Teresa.Lindqvist@calvoterra-mail.example</p></div>
    </div>
  </section>

  <section class="card card--split-right split">
    <div class="panel-green"></div>
    <div class="brand-tile"><span class="brand-tile__dot"></span><span class="brand-tile__name">Calvoterra</span></div>
    <div class="contact">
      <p class="contact__name">Teresa Lindqvist</p>
      <p class="contact__role">Marketing Director</p>
      <div class="contact__address"><p>CH-1563 Castelmont</p><p>Verdania</p></div>
      <div class="contact__reach"><p>+41 76 382 1904</p><p class="contact__email">Teresa.Lindqvist@calvoterra-mail.example</p></div>
    </div>
  </section>
</main>
</body>
</html>
```